Speisekarten-Design für italienisches Restaurant im Golfclub mit Blick auf die Alpen
Zielgruppe
Italienisches Restaurant im Golfclub mit Blick auf die Alpen (bei gutem Wetter)
Aufgabenstellung
Karte muss weiterhin bearbeitet werden könne. Es geht um ein Design das optisch anspricht aber nicht übertrieben ist. Die Blätter kommen später in eine Menukarte die noch in Auftrag gegeben werden.
Im Idealfall kann der Designer hierfür auch was mit designen das an einen Firma weitergeben werden kann um die 'Umschläge zu erstellen. Logo kann muss nicht mit drin sein. Es geht auch sehr um die einfache Darstellung des Ganzen.

```html
<!DOCTYPE html>
<html lang="de">
<head>
<meta charset="utf-8">
<title>Ristorante Vallora – Menükarte</title>
<link rel="stylesheet" href="https://fonts.googleapis.com/css2?family=Archivo:wght@400&family=Oswald:wght@400;600&display=swap">
<style>
  :root {
    --paper: #f0ebe1;
    --header: #231f20;
    --ink: #414042;
    --gold: #c9a04a;
    --price-box: #e0d9c5;
    --rule: #c8bea9;
    --illustration-a: #d9d4ca;
    --illustration-b: #ebe6dc;
  }
  html, body {
    margin: 0;
    padding: 0;
    overflow: hidden;
  }
  .menu-card {
    position: relative;
    width: 735px;
    height: 1200px;
    background: var(--paper);
    overflow: hidden;
    font-family: "Archivo", Arial, sans-serif;
    color: var(--ink);
  }
  .masthead {
    position: absolute;
    left: 0;
    top: 0;
    width: 735px;
    height: 180px;
    background: var(--header);
    display: flex;
    align-items: center;
    justify-content: center;
  }
  .masthead__name {
    font-family: "Oswald", Arial, sans-serif;
    font-weight: 400;
    font-size: 30px;
    letter-spacing: 4px;
    color: var(--gold);
    text-transform: uppercase;
    text-align: center;
    line-height: 1.2;
  }
  .masthead__name small {
    display: block;
    font-size: 10px;
    letter-spacing: 4px;
  }
  .course {
    position: absolute;
    left: 85px;
    width: 580px;
  }
  .course__title {
    margin: 0;
    font-family: "Oswald", Arial, sans-serif;
    font-weight: 600;
    font-size: 49px;
    line-height: 1;
    letter-spacing: -0.5px;
    color: var(--ink);
    transform: scaleX(0.92);
    transform-origin: left;
  }
  .course__dishes {
    list-style: none;
    margin: 0;
    padding: 0;
    position: absolute;
    left: 0;
    width: 360px;
  }
  .course__dishes li {
    font-size: 13px;
    line-height: 31.5px;
    white-space: nowrap;
  }
  .course__dishes li.dish--long {
    white-space: normal;
    line-height: 16px;
    padding: 8px 0 7.5px;
  }
  .course__price {
    position: absolute;
    left: 442px;
    width: 108px;
    height: 108px;
    background: var(--price-box);
    display: flex;
    align-items: center;
    justify-content: center;
    font-family: "Oswald", Arial, sans-serif;
    font-weight: 600;
    font-size: 45px;
    color: var(--ink);
  }
  .course__rule {
    position: absolute;
    left: 85px;
    width: 580px;
    height: 1px;
    background: var(--rule);
  }
  .produce-illustration {
    position: absolute;
    left: 29px;
    top: 1012px;
    width: 688px;
    height: 160px;
    background: linear-gradient(180deg, var(--illustration-b), var(--illustration-a) 60%, var(--illustration-b));
    border-radius: 40px;
  }
  .footer-band {
    position: absolute;
    left: 167px;
    top: 1150px;
    width: 402px;
    height: 50px;
    background: var(--price-box);
  }
</style>
</head>
<body>
<main class="menu-card">
  <header class="masthead">
    <div class="masthead__name">Ristorante Vallora<small>im Golfclub Sonnhalde</small></div>
  </header>

  <section class="course" style="top:276px">
    <h2 class="course__title">MENU 1</h2>
    <ul class="course__dishes" style="top:50px">
      <li>Appetithäppchen und Aperitif</li>
      <li>Italiensicher Aufschnitt Teller</li>
      <li>Pasta mit Hackfleischsoße und Sahne</li>
      <li>Kalbsbraten mit Barolosoße und Rosmarin Kartoffeln</li>
      <li>Zitronen Sorbet</li>
    </ul>
    <div class="course__price" style="top:8px">49,-</div>
  </section>
  <div class="course__rule" style="top:496px"></div>

  <section class="course" style="top:530px">
    <h2 class="course__title">MENU 2</h2>
    <ul class="course__dishes" style="top:54px">
      <li>Gemischter Salat</li>
      <li>Pasta mit scharfer Tomatensoße</li>
      <li>Putengeschnetzeltes in Currysoße mit Reis</li>
      <li>Tiramisu</li>
    </ul>
    <div class="course__price" style="top:9px">35,-</div>
  </section>
  <div class="course__rule" style="top:716px"></div>

  <section class="course" style="top:746px">
    <h2 class="course__title">MENU 3</h2>
    <ul class="course__dishes" style="top:46px">
      <li>Aperitif</li>
      <li>Vitello Tonnato</li>
      <li>Lasagne im Ofen überbacken</li>
      <li class="dish--long">Rumpsteak tranchiert, auf Rucola Bett serviert mit gehobelten Original Parmesan Käse</li>
      <li>Rosmarinkartoffeln und Gemüse</li>
      <li>Panna Cotta mit Waldfrüchte</li>
    </ul>
    <div class="course__price" style="top:16px">55,-</div>
  </section>

  <div class="footer-band"></div>
  <div class="produce-illustration" role="img" aria-label="Gezeichnete Gemüse-Illustration: Zwiebeln, Paprika, Knoblauch, Chilis, Golfball, Erbsen, Auberginen, Karotten und Kartoffeln"></div>
</main>
</body>
</html>
```